Tapwell Systems sales flyer for the licensed trade tri fold a4 leaflet style

Looking for a flyer / brochure to advertise our company service, needs to be modern and eye catching, aimed at licensee's and publicans. Our company saves them money on their beer losses.
I have attached some pictures which we use and our logo.
I have also attached leaflet that our parent company uses which contains more information.
Here are some key points
We are the originators of the specialist extended line cleaning service.
Our unique service allows for line cleaning to be extended from once every 7 days to once every 21 days.
We have provided our unique service since 1994
We guarantee our customers a minimum saving of 40% on their losses.
We are the only company to have been tested and proved by Barquell and Halden to improve quality and reduce costs.
Our web address is www.tapwellsystemsuk.example if you need info.

Industry/Entity Type

It Company

Font styles to use
Sans Serif

Colors
fbee3d
ffffff
fece3e
fbed22
fbf289

Requirements
Must have
• We are the originators of the specialist extended line cleaning service.
• Our unique service allows for line cleaning to be extended from once every 7 days to once every 21 days.
• We have provided our unique service since 1994
• We guarantee our customers a minimum saving of 40% on their losses.
• We are the only company to have been tested and proved by Barquell and Halden to improve quality and reduce costs.

```html
<!DOCTYPE html>
<html lang="en">
<head>
<meta charset="utf-8">
<title>Tapwell Systems – Tri-fold Leaflet</title>
<link href="https://fonts.googleapis.com/css2?family=Crimson+Text:ital,wght@0,400;0,600;0,700;1,700&family=Open+Sans:wght@400;600&display=swap" rel="stylesheet">
<style>
  :root{
    --red:#a3222c;
    --yellow:#f7e32b;
    --ink:#2a2a2a;
    --white:#ffffff;
    --stage:#3b3b3d;
  }
  *{margin:0;padding:0;box-sizing:border-box}
  html,body{width:1200px;height:784px;overflow:hidden;background:var(--stage)}
  .leaflet{position:absolute;left:50px;top:0;width:1100px;height:784px;background:var(--white);overflow:hidden;font-family:"Open Sans",Arial,sans-serif;color:var(--ink)}
  .leaflet-shapes{position:absolute;inset:0}

  .photo{position:absolute}
  .photo-bar-glass{left:505px;top:250px;width:150px;height:230px;border-radius:40px 40px 20px 20px;background:linear-gradient(180deg,#f4f4f4 0%,#e2d3a8 30%,#d7b873 100%);opacity:.3}
  .photo-pint{left:739px;top:205px;width:361px;height:410px;background:radial-gradient(ellipse at 45% 55%,#e0a630 0%,#9a5f17 28%,#3a2a20 60%,#1e1b1f 100%)}
  .photo-glasses{top:582px;width:146px;height:170px;border-radius:4px;background:linear-gradient(180deg,#ffffff 0%,#f0b43a 18%,#e59a1d 70%,#f3f0ea 100%)}
  .glasses-left{left:25px}
  .glasses-right{left:194px}

  .why{position:absolute;left:26px;top:96px;width:330px}
  .why-title{font-family:"Crimson Text",Georgia,serif;font-style:italic;font-weight:700;color:var(--red);font-size:26px;text-align:center;letter-spacing:.5px;margin-bottom:6px}
  .why-list{list-style:none}
  .why-list li{position:relative;padding-left:12px;font-size:9.6px;line-height:1.32;margin-bottom:6px}
  .why-list li::before{content:"";position:absolute;left:0;top:3px;width:5px;height:7px;background:var(--ink)}

  .brand{position:absolute;display:flex;flex-direction:column;align-items:center;font-family:"Crimson Text",Georgia,serif;color:var(--ink)}
  .brand-name{font-size:27px;font-weight:400;line-height:1.1}
  .brand-mark{display:block;width:14px;height:14px;border-radius:50%;background:var(--red);margin-top:10px}
  .brand-middle{left:373px;width:366px;top:320px}
  .brand-right{left:739px;width:361px;top:70px}

  .enquiry{position:absolute;left:373px;width:366px;top:470px;text-align:center;font-family:"Crimson Text",Georgia,serif;color:var(--red);font-size:17px;font-weight:600;line-height:1.35}
  .enquiry-phone{position:absolute;left:373px;width:366px;top:540px;text-align:center;font-size:26px;font-weight:600;color:#111;letter-spacing:.5px}

  .address{position:absolute;left:450px;top:652px;width:190px;text-align:center;font-style:normal;font-size:10px;line-height:1.5;color:#3a2a10}
  .address-name{font-family:"Crimson Text",Georgia,serif;color:var(--red);font-size:14px;font-weight:600}
  .contact-line{display:flex;align-items:center;justify-content:center;gap:5px}
  .contact-dot{width:7px;height:7px;border-radius:50%;background:var(--red);flex:none}

  .headline{position:absolute;left:739px;width:361px;top:646px;text-align:center;font-family:"Crimson Text",Georgia,serif}
  .headline-main{font-style:italic;font-weight:700;color:var(--white);font-size:24px;line-height:1.3;letter-spacing:1px;text-transform:uppercase}
  .headline-sub{color:var(--yellow);font-weight:600;font-size:16px;line-height:1.4;margin-top:6px}
</style>
</head>
<body>
<main class="leaflet">
  <svg class="leaflet-shapes" width="1100" height="784" viewBox="0 0 1100 784" aria-hidden="true">
    <defs>
      <linearGradient id="panelGrey" x1="0" y1="0" x2="0" y2="1">
        <stop offset="0" stop-color="#dcdddf"/>
        <stop offset="1" stop-color="#f4f4f5"/>
      </linearGradient>
    </defs>
    <path d="M0,0 H373 V110 C260,40 120,30 0,50 Z" fill="url(#panelGrey)"/>
    <path d="M0,44 C130,20 270,40 373,108 C270,62 130,56 0,68 Z" fill="var(--red)"/>
    <path d="M0,68 C130,56 270,62 373,108 L373,112 C270,68 130,62 0,72 Z" fill="var(--yellow)"/>
    <rect x="373" y="0" width="727" height="784" fill="url(#panelGrey)"/>
  </svg>

  <div class="photo photo-bar-glass" role="img" aria-label="Faint photo of a frothy pint glass behind the company name"></div>
  <div class="photo photo-pint" role="img" aria-label="Photo of a tall glass of golden lager on a bar"></div>
  <div class="photo photo-glasses glasses-left" role="img" aria-label="Photo of a row of lager glasses"></div>
  <div class="photo photo-glasses glasses-right" role="img" aria-label="Photo of a row of lager glasses"></div>

  <svg class="leaflet-shapes" width="1100" height="784" viewBox="0 0 1100 784" aria-hidden="true">
    <defs>
      <linearGradient id="foldShade" x1="0" y1="0" x2="1" y2="0">
        <stop offset="0" stop-color="#000" stop-opacity="0"/>
        <stop offset=".5" stop-color="#000" stop-opacity=".08"/>
        <stop offset="1" stop-color="#000" stop-opacity="0"/>
      </linearGradient>
    </defs>
    <path d="M440,255 C560,175 660,160 760,160 C900,160 1000,170 1100,175 L1100,218 C1000,212 900,206 790,205 C660,204 560,215 440,255 Z" fill="var(--red)"/>
    <path d="M440,255 C560,215 660,204 790,205 C900,206 1000,212 1100,218 L1100,226 C1000,220 900,214 790,212 C660,211 560,222 440,255 Z" fill="var(--yellow)"/>
    <path d="M373,585 C500,555 640,580 739,606 C850,578 990,560 1100,560 L1100,784 L373,784 Z" fill="var(--yellow)"/>
    <path d="M373,597 C500,567 640,592 739,618" stroke="var(--white)" stroke-width="3" fill="none"/>
    <path d="M590,784 C650,700 720,650 830,630 C940,612 1030,612 1100,616 L1100,784 Z" fill="var(--red)"/>
    <path d="M590,784 C650,700 720,650 830,630 C940,612 1030,612 1100,616" stroke="var(--white)" stroke-width="3" fill="none"/>
    <rect x="363" y="0" width="20" height="784" fill="url(#foldShade)"/>
    <rect x="729" y="0" width="20" height="784" fill="url(#foldShade)"/>
  </svg>

  <section class="why">
    <h2 class="why-title">WHY TSUK?</h2>
    <ul class="why-list">
      <li>Tapwell Systems (UK) are the originators of the extended beer line cleaning and cellar maintenance service which we have provided since 1994.</li>
      <li>We have been independently tested by laboratories and trade organisations and are the only service to be tested by Barquell, the largest technical service company in the UK, and Halden Brewers.</li>
      <li>The test results consistently prove that our service improves and maintains quality and reduces costs for the customer.</li>
      <li>Tapwell Systems (UK) provide a free survey and fixed price quotation for our service.</li>
      <li>Further savings are made as we provide our own chemicals and do not require the use of your gas or electricity.</li>
      <li>Tapwell Systems (UK) always guarantee our customers total satisfaction, we do not ask them to sign a contract or make any upfront payments or rental agreements.</li>
      <li>Our service has been tested and proved to work on all types of brewery dispense products.</li>
      <li>We provide our service to any trade account which provide draft products for their customers I.E Pubs, clubs, leisure centres and hotels etc.</li>
      <li>Tapwell Systems (UK) guarantee our customers a minimum of 40% savings on their existing weekly cleaning losses. We save our customers a minimum of 150 hours per year by providing our service for them.</li>
      <li>Our technicians carry out a series of preventative maintenance service checks during our visits, to ensure the correct operation of the cellar and dispense equipment.</li>
    </ul>
  </section>

  <div class="brand brand-middle">
    <div class="brand-name">Tapwell Systems (UK)</div>
    <span class="brand-mark"></span>
  </div>

  <p class="enquiry">For Further information or<br>to arrange a free survey and quotation<br>Please contact</p>
  <p class="enquiry-phone">01632 960418</p>

  <address class="address">
    <div class="address-name">Tapwell Systems (UK)</div>
    <div class="contact-line"><span class="contact-dot"></span>Unit 4 Brookfield Yard</div>
    <div>Llanwerin, Glenmoor</div>
    <div>GM12 4TQ</div>
    <div class="contact-line"><span class="contact-dot"></span>info@tapwellsystems.example</div>
    <div class="contact-line"><span class="contact-dot"></span>www.tapwellsystemsuk.example</div>
  </address>

  <div class="brand brand-right">
    <div class="brand-name">Tapwell Systems (UK)</div>
    <span class="brand-mark"></span>
  </div>

  <div class="headline">
    <h1 class="headline-main">Improved quality<br>and reduced costs</h1>
    <p class="headline-sub">Tested and proved by Barquell LTD<br>and Halden Brewers</p>
  </div>
</main>
</body>
</html>
```